Brand New Product Needs Sales Focused Website Design

Looking for design of Homepage, Category Page & Product Page for single product sales focused website. TrundleCrate manufacture and distribute a brand new product to the market called FoldNest-Bin which is a super strong, re-useable, folding & stacking plastic box which can be seen on our current website www.foldnest-bin.example FoldNest-Bin was originally developed as an alternative to supermarket carrier bags and was pitched as a box for life against the other low end re-useable products. The original version was made from recycled plastic and pitched very much as environmental product. We are now taking a different direction and have re-designed the boxes in 5 bright and fashionable designs and although we still want the primary focus to be supermarket shopping we want to position the product as a design led, must have shopping and household accessory rather than a boring, cheap looking black plastic box. The new designs will still have the environmental benefits of being able to be re-used thousands of times and being 100% recyclable and save on the imminent 5p tax on carrier bags in the UK however the new designs will not be made from recycled material. Although the main use for FoldNest-Bin is supermarket shopping it has a multitude of other uses especially where you need temporary storage - laundry, back of the car, moving house/students, gardening, days out, home office filing (will take A4 file), recycling and much more - FoldNest-Bin is made out of super strong Polypropylene and can be easily washed and sanitised after use and can be folded and unfolded thousands of times and so will last for many years. FoldNest-Bin is a product that needs to be seen in action to be understood so the web design must quickly and easily communicate what FoldNest-Bin is and how it works - this can be done with video, images and copy. Our current website does not work for many reasons:- it is too busy, has too much information, tries too hard and ultimately isn't working. Any of the images off our current website can be supplied for use. Once the concept of the website is agreed I can get these photoshopped with the new designs. Pictures of new designs for reference will be attached to this brief. Ultimately we want the website to convert visitors to sales and therefore designers with a proven track record in this field are especially welcome to enter. We also have a Dropbox folder with over 100 product and situation images in - please send email address and we will send an invite to the folder. Due to Christmas period this competition will be run over 15 days however we may choose to extend the deadline to account for the non working days. Any questions feel free to ask - we will respond within 24 hours where possible.

```html
<!DOCTYPE html>
<html lang="en">
<head>
<meta charset="utf-8">
<title>FoldNest-Bin — Ingenious &amp; Practical</title>
<link href="https://fonts.googleapis.com/css2?family=Open+Sans:wght@400;600;700&family=Lato:wght@400;700&display=swap" rel="stylesheet">
<style>
:root{
  --green:#7db92f;
  --pink:#c0336e;
  --blue:#3b82c6;
  --blue-light:#5aa0dd;
  --dark:#3b3b3b;
  --darker:#2e2e2e;
  --nav:#4a4a4a;
  --text:#333;
  --muted:#777;
  --page:#efefef;
  --white:#fff;
}
*{box-sizing:border-box;margin:0;padding:0}
html,body{width:714px;height:1200px;overflow:hidden}
body{background:var(--page);font-family:"Open Sans",Arial,sans-serif;color:var(--text);position:relative}
.abs{position:absolute}
/* header */
.header{left:0;top:0;width:714px;height:53px;background:var(--white)}
.brand{left:86px;top:6px;display:flex;align-items:center;gap:8px}
.brand-mark{width:28px;height:28px;background:var(--blue);border-radius:4px}
.brand-name{font-family:"Lato",sans-serif;font-size:19px;font-weight:700;color:var(--blue);line-height:1}
.brand-tag{left:122px;top:30px;font-size:11px;color:#555;letter-spacing:.5px}
.social-label{left:488px;top:12px;font-size:7px;color:#999;letter-spacing:.5px}
.social{left:566px;top:7px;display:flex;gap:5px}
.social span{width:18px;height:18px;border-radius:50%;display:block}
.utility{left:384px;top:34px;font-size:7.5px;font-weight:700;color:#333;display:flex;gap:9px}
.utility i{font-style:normal;color:#aaa;font-weight:400}
/* nav */
.nav{left:0;top:53px;width:714px;height:27px;background:var(--nav)}
.nav ul{position:absolute;left:86px;top:0;display:flex;list-style:none;height:27px}
.nav li{font-size:9.5px;color:#fff;padding:0 11px;line-height:27px;border-right:1px solid #5d5d5d}
.search{left:482px;top:58px;width:128px;height:16px;background:#fff;border-radius:8px;font-size:6.5px;color:#aaa;padding:4px 8px}
/* hero */
.hero-bg{left:0;top:80px;width:714px;height:214px}
.hero-title{left:102px;top:143px;color:#fff;font-size:23px;line-height:1.1}
.hero-title b{font-weight:700}
.hero-sub{left:102px;top:170px;color:#fff;font-size:18px}
.hero-sub b{font-weight:700}
.hero-copy{left:102px;top:196px;width:230px;color:#fff;font-size:9.5px;line-height:1.35}
.btn{font-size:10px;color:#fff;text-align:center;border-radius:2px}
.btn-green{background:var(--green)}
.btn-pink{background:var(--pink)}
.hero-btn{left:102px;top:232px;width:98px;height:19px;line-height:19px}
.hero-photo{left:350px;top:84px;width:270px;height:180px;background:linear-gradient(135deg,#e4dccb,#cfc6b3 60%,#7fb8c6);border-radius:4px}
/* steps */
.steps-frame{left:86px;top:358px;width:542px;height:70px;background:var(--blue)}
.step-tab{top:334px;width:113px;height:25px;background:var(--green);color:#fff;font-size:10.5px;text-align:center;line-height:25px}
.step-card{top:364px;width:113px;height:57px;background:#fff}
.step-img{position:absolute;left:30px;top:8px;width:54px;height:42px;background:linear-gradient(#2f63b8,#1d47a0)}
.step-num{top:366px;width:22px;height:22px;border-radius:50%;background:var(--green);border:2px solid #fff;color:#fff;font-size:11px;text-align:center;line-height:18px}
/* magic */
.panel{background:var(--white)}
.section-title{font-size:16px;letter-spacing:1px;color:#222}
.section-title span{color:var(--pink);font-weight:600}
.made-title{font-size:14px;letter-spacing:1px;line-height:1.3;white-space:nowrap;color:#222}
.body-copy{font-size:8.5px;line-height:1.75;color:#333}
.magic-photo{left:382px;top:447px;width:232px;height:120px;background:linear-gradient(135deg,#d9d2c4,#9a9a9a 50%,#a7d36a)}
.thumbs{left:382px;top:572px;display:flex;gap:7px}
.thumbs span{width:52px;height:32px;display:block;background:linear-gradient(135deg,#8b8b8b,#3b6fc1)}
.readmore{width:97px;height:19px;line-height:19px}
/* made */
.made-photo{left:390px;top:624px;width:230px;height:222px;background:linear-gradient(180deg,#efe8e4,#d9a78c 40%,#2fa56d 70%,#222)}
/* awards */
.award{top:906px;width:100px;text-align:center}
.award-disc{width:54px;height:54px;border-radius:50%;margin:0 auto 6px;display:flex;align-items:center;justify-content:center}
.award-name{font-size:7.5px;color:var(--blue);line-height:1.3}
.award-desc{font-size:6.5px;color:#333;line-height:1.4;margin-top:4px}
.avatar{left:398px;top:910px;width:68px;height:68px;border-radius:50%;border:4px solid #ddd;background:linear-gradient(#6d4c8f,#3e3a6d)}
.testi-name{left:474px;top:914px;font-size:8px;font-weight:700}
.testi-role{left:474px;top:926px;font-size:8.5px;color:var(--pink);font-weight:600}
.testi-copy{font-size:6.8px;line-height:1.35;color:#555}
/* footer */
.footer{left:0;top:1056px;width:714px;height:114px;background:var(--dark)}
.foot-head{font-size:7.5px;color:#ddd;font-weight:600;letter-spacing:.3px}
.foot-list{list-style:none;font-size:7px;color:#999;line-height:14px}
.foot-list li::before{content:"› ";color:#ccc}
.contact{font-size:7px;color:#999;line-height:1.4}
.foot-brand{left:492px;top:1094px;font-family:"Lato",sans-serif;font-size:16px;font-weight:700;color:#fff}
.foot-tag{left:492px;top:1114px;font-size:10px;color:#ddd;letter-spacing:.5px}
.foot-social{left:510px;top:1140px;display:flex;gap:4px;align-items:center;font-size:7px;color:#aaa}
.foot-social span{width:14px;height:14px;border-radius:50%;border:1px solid #999;display:block}
.bottom{left:0;top:1170px;width:714px;height:30px;background:var(--darker);font-size:6.5px;color:#aaa}
</style>
</head>
<body>

<header class="abs header"></header>
<div class="abs brand"><span class="brand-mark"></span><span class="brand-name">FoldNest-Bin</span></div>
<div class="abs brand-tag">Ingenious &amp; Practical</div>
<div class="abs social-label">SOCIALIZE WITH US :</div>
<div class="abs social"><span style="background:#3aa8dc"></span><span style="background:#c9333e"></span><span style="background:#3b5c9a"></span></div>
<div class="abs utility"><span>100% Guaranteed Returns</span><i>/</i><span>Sign In</span><i>/</i><span>Order Status</span><i>/</i><span>2.555.014.2290</span></div>

<nav class="abs nav"><ul><li>Home</li><li>What do you Think</li><li>Plastic Polution</li><li>Video</li><li>Gurantee</li><li>Buy</li></ul></nav>
<div class="abs search">SEARCH...</div>

<svg class="abs hero-bg" width="714" height="214" viewBox="0 0 714 214">
  <rect width="714" height="214" fill="#e9e9e9"/>
  <polygon points="0,0 86,0 86,160 0,190" fill="#3b82c6"/>
  <polygon points="628,0 714,0 714,195 628,165" fill="#3b82c6"/>
  <polygon points="0,0 40,0 0,60" fill="#5aa0dd"/>
  <polygon points="714,0 680,0 714,70" fill="#5aa0dd"/>
  <rect x="86" y="0" width="542" height="214" fill="#303030"/>
  <polygon points="86,0 628,0 628,202 86,202" fill="#2b2b2b"/>
  <polygon points="86,186 628,186 628,214 86,214" fill="#4a4a4a"/>
  <polygon points="86,148 300,176 357,200 414,176 628,148 628,160 414,188 357,212 300,188 86,160" fill="#3b82c6"/>
  <polygon points="300,176 357,200 414,176 357,190" fill="#5aa0dd"/>
</svg>
<svg class="abs" style="left:336px;top:302px" width="48" height="8" viewBox="0 0 48 8">
  <circle cx="6" cy="4" r="3" fill="#fff"/><circle cx="16" cy="4" r="3" fill="#aaa"/><circle cx="26" cy="4" r="3" fill="#aaa"/><circle cx="36" cy="4" r="3" fill="#aaa"/>
</svg>
<div class="abs hero-photo" role="img" aria-label="Floral patterned FoldNest-Bin folding box with a name label"></div>
<div class="abs hero-title">A best <b>Folding Box</b></div>
<div class="abs hero-sub">For You <b>Home</b> and <b>Offices</b></div>
<div class="abs hero-copy">es This Really Is A Simple Basic Product But Oh So Useful !! Our Existing Customers Have Become Real</div>
<div class="abs btn btn-green hero-btn">Discover more</div>

<div class="abs steps-frame"></div>
<div class="abs step-tab" style="left:107px">Folded Box</div>
<div class="abs step-tab" style="left:235px">Open The Clip</div>
<div class="abs step-tab" style="left:363px">Pull out Ends</div>
<div class="abs step-tab" style="left:491px">Stack Out</div>
<div class="abs step-card" style="left:107px"><div class="step-img" role="img" aria-label="Folded box, flat"></div></div>
<div class="abs step-card" style="left:235px"><div class="step-img" role="img" aria-label="Clip opened on the box"></div></div>
<div class="abs step-card" style="left:363px"><div class="step-img" role="img" aria-label="Ends pulled out of the box"></div></div>
<div class="abs step-card" style="left:491px"><div class="step-img" role="img" aria-label="Box standing open"></div></div>
<div class="abs step-num" style="left:97px">1</div>
<div class="abs step-num" style="left:213px">2</div>
<div class="abs step-num" style="left:343px">3</div>
<div class="abs step-num" style="left:476px">4</div>
<svg class="abs" style="left:200px;top:372px" width="340" height="30" viewBox="0 0 340 30" fill="none" stroke="#222" stroke-width="2">
  <path d="M12 14 Q22 4 32 14 l-4 -5 M32 14 l-6 1"/>
  <path d="M140 14 Q150 4 160 14 l-4 -5 M160 14 l-6 1"/>
  <path d="M268 14 Q278 4 288 14 l-4 -5 M288 14 l-6 1"/>
</svg>

<section class="abs panel" style="left:86px;top:432px;width:542px;height:180px"></section>
<div class="abs section-title" style="left:98px;top:447px">Its Magic <span>Open From This !</span></div>
<p class="abs body-copy" style="left:98px;top:479px;width:252px">Yes This Really Is A Simple Basic Product But Oh So Useful !! Our Existing Customers Have Become Real Fans Describing FoldNest-Bin As Innovative, Useful, Practical, Multipurpose, Unique, Ingenious, Clever, Functional And Most Pleasing Of All Great Value For Money.</p>
<div class="abs btn btn-pink readmore" style="left:98px;top:580px">Read More</div>
<div class="abs magic-photo" role="img" aria-label="Woman loading FoldNest-Bin boxes into a car boot, with green speech bubbles"></div>
<div class="abs thumbs" role="img" aria-label="Four small photos of the box in use"><span></span><span></span><span></span><span></span></div>

<section class="abs" style="left:86px;top:624px;width:542px;height:222px;background:#f4f4f4"></section>
<div class="abs made-title" style="left:100px;top:643px">Design and Made in britian from 100% Recyled<br>Material &amp; IS100% Recyicleable !</div>
<p class="abs body-copy" style="left:99px;top:688px;width:266px;line-height:1.55">FoldNest-Bin is a practical folding box which can be use countless times for a variety of everyday tasks.  Terrific to take with you on your regular grocery shop.  The featherlight "briefcase" format means it's easy to carry one or several into the store.<br><br>Open at the checkout in seconds, fill and stack if you have a heavy load of shopping.  Then it's out to the car.</p>
<div class="abs btn btn-pink readmore" style="left:96px;top:804px">Read More</div>
<div class="abs made-photo" role="img" aria-label="Smiling woman in a green top holding an open black folding box"></div>

<section class="abs panel" style="left:86px;top:846px;width:542px;height:210px"></section>
<div class="abs section-title" style="left:100px;top:866px">Awards Winning Products</div>
<div class="abs section-title" style="left:396px;top:866px">Our Testimonials</div>

<div class="abs award" style="left:84px">
  <div class="award-disc" style="background:var(--pink)"><svg width="26" height="28" viewBox="0 0 26 28" fill="#fff"><path d="M5 2h16v8a8 8 0 0 1-16 0z"/><path d="M5 4H1a5 5 0 0 0 5 6M21 4h4a5 5 0 0 1-5 6" fill="none" stroke="#fff" stroke-width="2"/><rect x="11" y="17" width="4" height="5"/><rect x="7" y="22" width="12" height="4"/></svg></div>
  <div class="award-name">Fenbridge<br>Evening Post</div>
  <div class="award-desc">Best New Business Idea<br>Of The Yea</div>
</div>
<div class="abs award" style="left:177px">
  <div class="award-disc" style="background:#1e1e1e"><svg width="26" height="28" viewBox="0 0 26 28" fill="#fff"><path d="M5 2h16v8a8 8 0 0 1-16 0z"/><path d="M5 4H1a5 5 0 0 0 5 6M21 4h4a5 5 0 0 1-5 6" fill="none" stroke="#fff" stroke-width="2"/><rect x="11" y="17" width="4" height="5"/><rect x="7" y="22" width="12" height="4"/></svg></div>
  <div class="award-name">Hardware Traders<br>Guild</div>
  <div class="award-desc">Best New Product of The<br>Year Supreme Sword Of<br>Achievement</div>
</div>
<div class="abs award" style="left:270px">
  <div class="award-disc" style="background:#1e1e1e"><svg width="26" height="28" viewBox="0 0 26 28" fill="#fff"><path d="M5 2h16v8a8 8 0 0 1-16 0z"/><path d="M5 4H1a5 5 0 0 0 5 6M21 4h4a5 5 0 0 1-5 6" fill="none" stroke="#fff" stroke-width="2"/><rect x="11" y="17" width="4" height="5"/><rect x="7" y="22" width="12" height="4"/></svg></div>
  <div class="award-name">Tomorrow's Ideas<br>Show</div>
  <div class="award-desc">Royal Innovation Award<br>For Technical<br>Innovation-Finalist</div>
</div>

<div class="abs avatar" role="img" aria-label="Customer portrait"></div>
<div class="abs testi-name">Marla Quinn</div>
<div class="abs testi-role">Situet amet lipsum dolor</div>
<p class="abs testi-copy" style="left:474px;top:942px;width:140px">Lorem ipsum dolor sit amet, consectetur adipiscing elit. Fusce elementum, nulla vel pellentesque consequat, ante nulla</p>
<p class="abs testi-copy" style="left:401px;top:983px;width:214px">Lorem ipsum dolor sit amet, consectetur adipiscing elit. Fusce elementum, nulla vel pellentesque consequat, ante nulla</p>
<div class="abs btn btn-pink" style="left:523px;top:1013px;width:88px;height:17px;line-height:17px">View all</div>

<footer class="abs footer"></footer>
<div class="abs foot-head" style="left:86px;top:1078px">WHO WE ARE</div>
<ul class="abs foot-list" style="left:86px;top:1093px"><li>About Us</li><li>Products</li><li>News</li><li>Gallery</li></ul>
<div class="abs foot-head" style="left:198px;top:1078px">OUR SERVICES</div>
<ul class="abs foot-list" style="left:198px;top:1093px"><li>Concrete Sleepers</li><li>Concrete Retaining Walls</li><li>Concrete Plinths</li><li>Concrete Plinths</li></ul>
<div class="abs foot-head" style="left:338px;top:1078px">CONTACT US</div>
<svg class="abs" style="left:338px;top:1095px" width="10" height="62" viewBox="0 0 10 62" fill="#999">
  <path d="M5 0a4 4 0 0 1 4 4c0 3-4 7-4 7S1 7 1 4a4 4 0 0 1 4-4z"/>
  <path d="M2 24c1-1 3 0 3 1l-1 2c1 2 2 3 4 4l2-1c1 0 2 2 1 3-4 2-11-5-9-9z"/>
  <rect x="0" y="51" width="10" height="7"/><path d="M0 51l5 4 5-4" stroke="#3b3b3b" fill="none"/>
</svg>
<div class="abs contact" style="left:354px;top:1094px">Address: 1234 Street Name,<br>City, State 12354</div>
<div class="abs contact" style="left:354px;top:1121px;font-size:10px;color:#ccc">1233-555-0190</div>
<div class="abs contact" style="left:354px;top:1145px">info@domainname.com</div>
<div class="abs foot-brand">FoldNest-Bin</div>
<div class="abs foot-tag">Ingenious &amp; Practical</div>
<div class="abs foot-social">Follow us :<span></span><span></span><span></span><span></span><span></span></div>

<div class="abs bottom">
  <span style="position:absolute;left:78px;top:11px">Copyright © 2014 FOLDNEST-BIN, unless otherwise noted.</span>
  <span style="position:absolute;left:512px;top:11px;text-decoration:underline">Terms &amp; Conditions</span>
  <span style="position:absolute;left:579px;top:11px">|</span>
  <span style="position:absolute;left:585px;top:11px;text-decoration:underline">Privacy Policy</span>
</div>

</body>
</html>
```